Commercial Flow Chart-Early Out to Bad Debt

Need to update the attached flow chart to include another line of business.

Target Market(s)

Business to Business

```html
<!DOCTYPE html>
<html lang="en">
<head>
<meta charset="utf-8">
<title>Early Out to Collection Flow Chart</title>
<link href="https://fonts.googleapis.com/css2?family=Ubuntu:wght@400;500;700&family=Oswald:wght@600&family=Arimo:wght@700&display=swap" rel="stylesheet">
<style>
  :root {
    --maroon: #7f4a4b;
    --teal-dark: #2f5e5a;
    --graphite: #474747;
    --sage: #7fb8a0;
    --steel: #7eaab3;
    --paper: #f4f4f4;
    --paper-edge: #e6e6e6;
    --ink: #2b2b2b;
  }
  html, body {
    margin: 0;
    padding: 0;
    width: 1200px;
    height: 850px;
    overflow: hidden;
    background: var(--paper);
  }
  .flyer { display: block; width: 1200px; height: 850px; }
  .body-text { font-family: "Ubuntu", sans-serif; font-size: 17.5px; font-weight: 500; }
  .legal-note { font-family: "Arimo", sans-serif; font-size: 18.5px; font-weight: 700; fill: var(--maroon); }
  .brand-name { font-family: "Ubuntu", sans-serif; font-size: 25px; font-weight: 500; fill: var(--teal-dark); letter-spacing: 1px; }
  .hub-title { font-family: "Oswald", sans-serif; font-size: 27px; font-weight: 600; fill: #fff; }
  .hub-sub { font-family: "Ubuntu", sans-serif; font-size: 14px; font-weight: 500; fill: #fff; letter-spacing: 1px; }
  .site-url { font-family: "Ubuntu", sans-serif; font-size: 22px; font-weight: 400; fill: var(--ink); letter-spacing: 12px; }
  .t-maroon { fill: var(--maroon); }
  .t-teal { fill: var(--teal-dark); }
  .t-graphite { fill: var(--graphite); }
  .t-sage { fill: var(--sage); }
  .t-steel { fill: var(--steel); }
  .petal-maroon { fill: var(--maroon); }
  .petal-teal { fill: var(--teal-dark); }
  .petal-graphite { fill: var(--graphite); }
  .petal-sage { fill: var(--sage); }
  .petal-steel { fill: var(--steel); }
  .icon { fill: none; stroke: #fff; stroke-width: 1.4; stroke-linecap: round; stroke-linejoin: round; }
  .rule { stroke: var(--sage); stroke-width: 1.3; }
</style>
</head>
<body>
<svg class="flyer" viewBox="0 0 1200 850" xmlns="http://www.w3.org/2000/svg">
  <defs>
    <radialGradient id="paper-light" cx="50%" cy="50%" r="70%">
      <stop offset="0" stop-color="#fafafa"/>
      <stop offset="1" stop-color="#ebebeb"/>
    </radialGradient>
    <radialGradient id="gear-haze" cx="50%" cy="50%" r="50%">
      <stop offset="0" stop-color="#d9d9d9" stop-opacity="0.55"/>
      <stop offset="1" stop-color="#d9d9d9" stop-opacity="0"/>
    </radialGradient>

    <path id="petal" d="M -15,-86 C -6,-82 6,-82 15,-86 L 54,-186 C 60,-205 42,-218 0,-220 C -42,-218 -60,-205 -54,-186 Z"/>

    <symbol id="i-user" viewBox="0 0 24 24"><circle cx="12" cy="12" r="10"/><circle cx="12" cy="9.5" r="3.5"/><path d="M5.5 18.5c1.5-3 3.8-4.5 6.5-4.5s5 1.5 6.5 4.5"/></symbol>
    <symbol id="i-gauge" viewBox="0 0 24 24"><path d="M2 18a10 10 0 0 1 20 0z"/><path d="M5 18a7 7 0 0 1 14 0"/><path d="M12 18l4-4"/></symbol>
    <symbol id="i-docs" viewBox="0 0 24 24"><rect x="4" y="6" width="9" height="13"/><rect x="7" y="3" width="9" height="13"/><path d="M9 7h5M9 10h5M9 13h5M17 10h5M20 8l2 2-2 2"/></symbol>
    <symbol id="i-doc" viewBox="0 0 24 24"><path d="M5 2h10l4 4v16H5z"/><path d="M8 7h7M8 10h8M8 13h8M8 16h5M13 19l8-8"/></symbol>
    <symbol id="i-phone" viewBox="0 0 24 24"><path d="M22 16.9v3a2 2 0 0 1-2.2 2 19.8 19.8 0 0 1-8.6-3.1 19.5 19.5 0 0 1-6-6A19.8 19.8 0 0 1 2.1 4.2 2 2 0 0 1 4.1 2h3a2 2 0 0 1 2 1.7c.1.9.4 1.9.7 2.8a2 2 0 0 1-.5 2.1L8.1 9.9a16 16 0 0 0 6 6l1.3-1.3a2 2 0 0 1 2.1-.4c.9.3 1.9.6 2.8.7a2 2 0 0 1 1.7 2z"/><path d="M15 5a5 5 0 0 1 4 4M15 1a9 9 0 0 1 8 8"/></symbol>
    <symbol id="i-mobile" viewBox="0 0 24 24"><rect x="5" y="2" width="10" height="20" rx="1.5"/><path d="M5 5h10M5 18h10"/><rect x="11" y="9" width="9" height="7"/><path d="M11 9l4.5 4 4.5-4"/></symbol>
    <symbol id="i-gear" viewBox="0 0 24 24"><circle cx="12" cy="12" r="8"/><path d="M12 1v3M12 20v3M1 12h3M20 12h3M4.2 4.2l2.1 2.1M17.7 17.7l2.1 2.1M4.2 19.8l2.1-2.1M17.7 6.3l2.1-2.1"/><circle cx="12" cy="10.5" r="2.3"/><path d="M8 16c1-2 2.4-3 4-3s3 1 4 3"/></symbol>
    <symbol id="i-hand" viewBox="0 0 24 24"><circle cx="13" cy="6" r="4"/><path d="M13 4v4M11.8 5h2.2M12 7h2.2"/><path d="M2 17l4-4h5l3 1h-4M6 19l3-1h6l6-6"/><path d="M2 17l3 3"/></symbol>
    <symbol id="i-form" viewBox="0 0 24 24"><rect x="2" y="4" width="20" height="16"/><path d="M2 8h20M12 12h7M12 15h7"/><circle cx="7" cy="13" r="1.8"/><path d="M4.5 17c.6-1.2 1.5-1.8 2.5-1.8s1.9.6 2.5 1.8"/></symbol>
    <symbol id="i-gavel" viewBox="0 0 24 24"><rect x="6" y="2" width="12" height="6" rx="1"/><path d="M12 8v7"/><path d="M9 13h6v3H9zM2 17h5l2-1h3v4H7"/></symbol>
    <symbol id="i-scale" viewBox="0 0 24 24"><path d="M12 3v17M7 21h10M4 6h16"/><circle cx="12" cy="3" r="1"/><path d="M4 6l-3 7h6zM20 6l-3 7h6zM1 13a3 2 0 0 0 6 0M17 13a3 2 0 0 0 6 0"/></symbol>
    <symbol id="i-mail" viewBox="0 0 24 24"><path d="M2 9l10-6 10 6v13H2z"/><path d="M2 22l8-7h4l8 7M2 9l7 5M22 9l-7 5"/><path d="M6 4h12v8M9 7h6M9 9.5h6"/></symbol>
    <symbol id="i-send" viewBox="0 0 24 24"><path d="M8 12l8-8 7 7-8 8z"/><path d="M8 12l8 1 7-2M16 13l-1 6"/><path d="M1 8h5M2 12h4M1 16h5M3 20h6"/></symbol>
    <symbol id="i-stamp" viewBox="0 0 24 24"><rect x="6" y="2" width="15" height="20"/><path d="M10 6h7M10 9h7M14 12h3"/><circle cx="6" cy="12" r="2"/><path d="M5 14v3h2v-3M2 19h8v2H2z"/><circle cx="16" cy="17" r="2"/></symbol>
  </defs>

  <rect width="1200" height="850" fill="url(#paper-light)"/>

  <g role="img" aria-label="Faint interlocking gears decoration">
    <ellipse cx="1000" cy="150" rx="260" ry="200" fill="url(#gear-haze)"/>
  </g>
  <g role="img" aria-label="Faint interlocking gears decoration">
    <ellipse cx="150" cy="760" rx="220" ry="170" fill="url(#gear-haze)"/>
  </g>

  <g class="brand">
    <text class="brand-name" x="92" y="92">Summit</text>
    <text class="brand-name" x="92" y="122">Ledger</text>
    <text class="brand-name" x="92" y="152">Group</text>
  </g>

  <!-- Early out process -->
  <g class="hub early-out" transform="translate(447 421)">
    <g transform="rotate(-36)"><use href="#petal" class="petal-maroon"/><g transform="translate(0 -155) rotate(36)"><use href="#i-user" class="icon" x="-22" y="-22" width="44" height="44"/></g></g>
    <g transform="rotate(-64)"><use href="#petal" class="petal-teal"/><g transform="translate(0 -155) rotate(64)"><use href="#i-gauge" class="icon" x="-24" y="-24" width="48" height="48"/></g></g>
    <g transform="rotate(-94)"><use href="#petal" class="petal-sage"/><g transform="translate(0 -155) rotate(94)"><use href="#i-docs" class="icon" x="-22" y="-22" width="44" height="44"/></g></g>
    <g transform="rotate(-124)"><use href="#petal" class="petal-steel"/><g transform="translate(0 -155) rotate(124)"><use href="#i-doc" class="icon" x="-22" y="-22" width="44" height="44"/></g></g>
    <g transform="rotate(-153)"><use href="#petal" class="petal-graphite"/><g transform="translate(0 -155) rotate(153)"><use href="#i-phone" class="icon" x="-20" y="-20" width="40" height="40"/></g></g>
    <g transform="rotate(174)"><use href="#petal" class="petal-maroon"/><g transform="translate(0 -155) rotate(-174)"><use href="#i-mobile" class="icon" x="-22" y="-22" width="44" height="44"/></g></g>
    <g transform="rotate(143)"><use href="#petal" class="petal-teal"/><g transform="translate(0 -155) rotate(-143)"><use href="#i-gear" class="icon" x="-23" y="-23" width="46" height="46"/></g></g>

    <circle r="74" fill="var(--sage)"/>
    <circle r="66" fill="var(--maroon)"/>
    <text class="hub-title" y="4" text-anchor="middle">EARLY OUT</text>
    <text class="hub-sub" y="24" text-anchor="middle">PROCESS</text>
  </g>

  <!-- Collection process -->
  <g class="hub collection" transform="translate(764 465)">
    <g transform="rotate(-101)"><use href="#petal" class="petal-sage"/><g transform="translate(0 -155) rotate(101)"><use href="#i-form" class="icon" x="-22" y="-22" width="44" height="44"/></g></g>
    <g transform="rotate(-64)"><use href="#petal" class="petal-steel"/><g transform="translate(0 -155) rotate(64)"><use href="#i-hand" class="icon" x="-24" y="-24" width="48" height="48"/></g></g>
    <g transform="rotate(-35)"><use href="#petal" class="petal-graphite"/><g transform="translate(0 -155) rotate(35)"><use href="#i-gavel" class="icon" x="-24" y="-24" width="48" height="48"/></g></g>
    <g transform="rotate(-6)"><use href="#petal" class="petal-maroon"/><g transform="translate(0 -155) rotate(6)"><use href="#i-scale" class="icon" x="-22" y="-22" width="44" height="44"/></g></g>
    <g transform="rotate(25)"><use href="#petal" class="petal-teal"/><g transform="translate(0 -155) rotate(-25)"><use href="#i-mail" class="icon" x="-22" y="-22" width="44" height="44"/></g></g>
    <g transform="rotate(53)"><use href="#petal" class="petal-sage"/><g transform="translate(0 -155) rotate(-53)"><use href="#i-phone" class="icon" x="-22" y="-22" width="44" height="44"/></g></g>
    <g transform="rotate(84)"><use href="#petal" class="petal-steel"/><g transform="translate(0 -155) rotate(-84)"><use href="#i-send" class="icon" x="-24" y="-24" width="48" height="48"/></g></g>
    <g transform="rotate(117)"><use href="#petal" class="petal-graphite"/><g transform="translate(0 -155) rotate(-117)"><use href="#i-stamp" class="icon" x="-24" y="-24" width="48" height="48"/></g></g>

    <circle r="74" fill="var(--teal-dark)"/>
    <circle r="66" fill="var(--steel)"/>
    <text class="hub-title" y="4" text-anchor="middle">COLLECTION</text>
    <text class="hub-sub" y="24" text-anchor="middle">PROCESS</text>
  </g>

  <!-- Early out labels -->
  <text class="body-text t-maroon" text-anchor="end"><tspan x="270" y="220">Account is</tspan><tspan x="270" y="240">Received</tspan></text>
  <text class="body-text t-teal" style="font-weight:700"><tspan x="89" y="309">Skiptracing/</tspan><tspan x="89" y="332">Scoring Scrub</tspan></text>
  <text class="body-text t-sage" text-anchor="end"><tspan x="201" y="418">Letters with your</tspan><tspan x="201" y="441">company logo sent to</tspan><tspan x="201" y="464">debtor for payment</tspan></text>
  <text class="body-text t-steel" text-anchor="end"><tspan x="216" y="546">A series of</tspan><tspan x="216" y="566">3 letters are sent</tspan></text>
  <text class="body-text t-graphite" text-anchor="end"><tspan x="315" y="644">Phone calls/text</tspan><tspan x="315" y="665">messages weekly</tspan></text>
  <text class="body-text t-maroon"><tspan x="419" y="689">Emails are</tspan><tspan x="419" y="710">sent weekly</tspan></text>
  <text class="body-text t-teal"><tspan x="581" y="640">If account is</tspan><tspan x="581" y="660">not resolved</tspan><tspan x="581" y="681">within 60days of</tspan><tspan x="581" y="701">placement</tspan></text>

  <!-- Collection labels -->
  <text class="body-text t-sage"><tspan x="651" y="564">Account is moved</tspan><tspan x="651" y="584">to collections</tspan></text>
  <text class="body-text t-steel" text-anchor="end"><tspan x="551" y="329">Collections</tspan><tspan x="551" y="350">Begin</tspan></text>
  <text class="body-text t-graphite"><tspan x="475" y="242">Attorney will make</tspan><tspan x="475" y="264">demand on debtor</tspan></text>
  <text class="legal-note" text-anchor="middle"><tspan x="750" y="149">If client wants to pursue legal action</tspan><tspan x="750" y="172">involving courts, the attorney will proceed</tspan><tspan x="750" y="195">with judgment</tspan></text>
  <text class="body-text t-teal"><tspan x="891" y="221">A series of 3 more</tspan><tspan x="891" y="241">collection letters are sent</tspan></text>
  <text class="body-text t-sage"><tspan x="998" y="327">Collection</tspan><tspan x="998" y="347">Phone calls are</tspan><tspan x="998" y="368">made weekly</tspan></text>
  <text class="body-text t-steel"><tspan x="1026" y="455">Emails are</tspan><tspan x="1026" y="476">sent weekly</tspan></text>
  <text class="body-text t-graphite"><tspan x="1010" y="565">If account balance</tspan><tspan x="1010" y="588">warrants, SLG will</tspan><tspan x="1010" y="611">utilize our national</tspan><tspan x="1010" y="634">network of attorneys</tspan><tspan x="1010" y="657">to initiate legal</tspan><tspan x="1010" y="680">process</tspan></text>

  <!-- Footer -->
  <line class="rule" x1="90" y1="791" x2="308" y2="791"/>
  <line class="rule" x1="891" y1="791" x2="1110" y2="791"/>
  <text class="site-url" x="606" y="799" text-anchor="middle">www.summitledger.net</text>
</svg>
</body>
</html>
```